Business Card Design for Small Electrical Contractor

I need to update my business card into something a little more modern. We are a small electrical contracting company. We service domestic and commercial places around Sydney. We have 2 logo designs at the moment. I have uploaded both and 2 different sizes to work with.

Industry/Entity Type

Business

Contact Information for Business Card

Leo Hartigan
8/21-23 Birch Rd, Kelsworth 2087
t - (02) 9381 4720
m - 0427 815 903
E - info@hartiganelx.com.au
W - hartiganelx.com.au
ABN: 42 907 551 316

Font styles to use
Sans Serif

Requirements
Must have
• I would also like to see the below fit on somewhere aswell
• - Licensed Electrician
• - Level 2 (Cat 1 & 4)
• - Domestic
• - Commercial
• - Repairs and Installations
• - Data
Nice to have
• Try and keep similar colours as logo
Should not have
• No lightning bolts or light globes. Smart and professional please.

```html
<!DOCTYPE html>
<html lang="en">
<head>
<meta charset="utf-8">
<title>L&amp;K Hartigan Electrical – Business Card</title>
<link href="https://fonts.googleapis.com/css2?family=Montserrat:wght@400;500;600&display=swap" rel="stylesheet">
<style>
  :root {
    --green: #1f4a45;
    --green-deep: #183d39;
    --orange: #f39a1e;
    --white: #ffffff;
    --ink: #1e2b2a;
    --backdrop: #e8e5e0;
  }
  * { box-sizing: border-box; margin: 0; padding: 0; }
  html, body { width: 1200px; height: 900px; overflow: hidden; }
  body {
    background: var(--backdrop);
    font-family: "Montserrat", Arial, sans-serif;
    display: flex;
    align-items: center;
    justify-content: center;
    gap: 40px;
  }
  .card {
    position: relative;
    width: 540px;
    height: 330px;
    border-radius: 4px;
    overflow: hidden;
    box-shadow: 0 6px 18px rgba(0,0,0,0.15);
  }
  .card-shapes { position: absolute; inset: 0; }

  /* Back face */
  .card-back { background: var(--green); color: var(--white); }
  .card-back .brand-name {
    position: absolute; top: 100px; left: 0; right: 0;
    text-align: center; font-weight: 500; font-size: 30px; line-height: 1.2;
    color: var(--white);
  }
  .card-back .brand-rule {
    position: absolute; top: 192px; left: 110px; width: 330px; height: 1.5px;
    background: var(--orange);
  }
  .card-back .back-web {
    position: absolute; top: 248px; left: 0; right: 0;
    display: flex; justify-content: center; align-items: center; gap: 8px;
    color: var(--orange); font-size: 15px; font-weight: 500;
  }
  .card-back .bottom-rule {
    position: absolute; top: 290px; left: 40px; width: 460px; height: 1.5px;
    background: var(--orange);
  }
  .icon-chip {
    width: 14px; height: 14px; border-radius: 2px; background: var(--orange);
    display: inline-flex; align-items: center; justify-content: center; flex: none;
  }

  /* Front face */
  .card-front { background: var(--white); color: var(--ink); }
  .card-front .brand-name {
    position: absolute; top: 28px; right: 26px; text-align: right;
    font-weight: 500; font-size: 24px; line-height: 1.15; color: var(--green);
  }
  .card-front .brand-rule {
    position: absolute; top: 88px; right: 26px; width: 190px; height: 1.2px;
    background: var(--orange);
  }
  .card-front .abn {
    position: absolute; top: 95px; right: 60px; font-size: 9px; line-height: 12px; color: var(--ink);
  }
  .services {
    position: absolute; top: 116px; left: 36px; list-style: none;
    font-size: 13px; line-height: 19px; color: var(--ink);
  }
  .services li { display: flex; align-items: center; gap: 10px; }
  .services li::before {
    content: ""; width: 0; height: 0;
    border-top: 4px solid transparent; border-bottom: 4px solid transparent;
    border-left: 7px solid var(--orange);
  }
  .address {
    position: absolute; top: 272px; left: 36px; color: var(--white);
    font-size: 13px; line-height: 19px;
  }
  .person {
    position: absolute; top: 118px; right: 24px;
    display: flex; align-items: center; gap: 8px;
  }
  .person-name {
    color: var(--orange); font-weight: 600; font-size: 15px;
    font-variant: small-caps; letter-spacing: 0.5px;
  }
  .person-chip {
    width: 20px; height: 20px; border-radius: 3px; background: var(--green);
    display: flex; align-items: center; justify-content: center;
  }
  .contacts {
    position: absolute; top: 164px; right: 18px; list-style: none;
    color: var(--white); font-size: 11.5px; line-height: 19px; text-align: right;
  }
  .contacts li { display: flex; align-items: center; justify-content: flex-end; gap: 6px; }
</style>
</head>
<body>

  <section class="card card-back" aria-label="Card back">
    <div class="brand-name">L&amp;K Hartigan<br>Electrical</div>
    <div class="brand-rule"></div>
    <div class="back-web">
      <span class="icon-chip">
        <svg width="10" height="10" viewBox="0 0 10 10"><circle cx="5" cy="5" r="3.8" fill="none" stroke="#1f4a45" stroke-width="1"/><line x1="1.2" y1="5" x2="8.8" y2="5" stroke="#1f4a45" stroke-width="0.8"/></svg>
      </span>
      hartiganelx.com.au
    </div>
    <div class="bottom-rule"></div>
  </section>

  <section class="card card-front" aria-label="Card front">
    <svg class="card-shapes" width="540" height="330" viewBox="0 0 540 330">
      <polygon points="0,0 190,0 168,30 0,30" fill="#f39a1e"/>
      <rect x="0" y="232" width="320" height="22" fill="#f39a1e"/>
      <rect x="0" y="262" width="320" height="68" fill="#1f4a45"/>
      <polygon points="352,148 540,148 540,330 330,330 330,170" fill="#1f4a45"/>
    </svg>

    <div class="brand-name">L&amp;K Hartigan<br>Electrical</div>
    <div class="brand-rule"></div>
    <div class="abn">ABN: 42 907 551 316</div>

    <ul class="services">
      <li>Licensed Electrician</li>
      <li>Level 2 (Cat 1 &amp; 4)</li>
      <li>Domestic</li>
      <li>Commercial</li>
      <li>Repairs and Installations</li>
      <li>Data</li>
    </ul>

    <div class="address">8/21-23 Birch Rd,<br>Kelsworth 2087</div>

    <div class="person">
      <span class="person-name">Leo Hartigan</span>
      <span class="person-chip">
        <svg width="12" height="12" viewBox="0 0 12 12"><circle cx="6" cy="4" r="2.3" fill="#fff"/><path d="M1.5 11.5 a4.5 4 0 0 1 9 0z" fill="#fff"/></svg>
      </span>
    </div>

    <ul class="contacts">
      <li>(02) 9381 4720
        <span class="icon-chip"><svg width="9" height="9" viewBox="0 0 10 10"><path d="M2 1 L4 1 L4.6 3 L3.4 4 Q4.5 6 6 6.6 L7 5.4 L9 6 L9 8 Q5 9 1.5 5 Q1 3 2 1z" fill="#1f4a45"/></svg></span>
      </li>
      <li>0427 815 903
        <span class="icon-chip"><svg width="9" height="9" viewBox="0 0 10 10"><rect x="2.5" y="0.8" width="5" height="8.4" rx="1" fill="none" stroke="#1f4a45" stroke-width="1.1"/><circle cx="5" cy="7.6" r="0.6" fill="#1f4a45"/></svg></span>
      </li>
      <li>info@hartiganelx.com.au
        <span class="icon-chip"><svg width="9" height="9" viewBox="0 0 10 10"><rect x="1" y="2.5" width="8" height="5.5" fill="none" stroke="#1f4a45" stroke-width="1"/><path d="M1 2.5 L5 5.6 L9 2.5" fill="none" stroke="#1f4a45" stroke-width="1"/></svg></span>
      </li>
      <li>hartiganelx.com.au
        <span class="icon-chip"><svg width="9" height="9" viewBox="0 0 10 10"><circle cx="5" cy="5" r="3.8" fill="none" stroke="#1f4a45" stroke-width="1"/><line x1="1.2" y1="5" x2="8.8" y2="5" stroke="#1f4a45" stroke-width="0.8"/></svg></span>
      </li>
    </ul>
  </section>

</body>
</html>
```